App Design for quiz app (casual gaming app)

We need an design & logo for our quiz app. Its a simple quiz app, where you pick up a category, answer three questions out of this category. After this an opponent is assigned to your game, and has to answer the same three questions. After this first round is finished, it's the opponents turn to choose a new category and answer three questions out of this category. Now it's your turn to answer the same three questions. With this done, the 2nd round is finished. One game has seven rounds.
Please find attached the balsamiq project. For all of you, do not have balsamiq, please find also the mockups as pdf.
Final delivery should be psd files
Target Market(s)
Casual Games

```html
<!DOCTYPE html>
<html lang="en">
<head>
<meta charset="utf-8">
<title>Quiz App – Overview Screens</title>
<link href="https://fonts.googleapis.com/css2?family=Lato:ital,wght@0,300;0,400;0,700;1,300;1,400;1,700&display=swap" rel="stylesheet">
<style>
  :root {
    --page-bg: #efebe7;
    --status-bg: #000000;
    --header-bg: #ececec;
    --list-bg: #ffffff;
    --accent: #a9cbd6;
    --text-dark: #333333;
    --text-muted: #9a9a9a;
    --divider: #dcdcdc;
    --menu-bg: rgba(52, 52, 52, 0.86);
    --white: #ffffff;
    --avatar-a: #e2b27a;
    --avatar-b: #b0703c;
  }
  * { box-sizing: border-box; margin: 0; padding: 0; }
  html, body { width: 1158px; height: 1200px; overflow: hidden; }
  body {
    background: var(--page-bg);
    font-family: "Lato", sans-serif;
    position: relative;
  }
  .screen {
    position: absolute;
    top: 171px;
    width: 480px;
    height: 857px;
    background: var(--list-bg);
    overflow: hidden;
  }
  .screen--home { left: 69px; }
  .screen--menu { left: 609px; }

  .status-bar {
    height: 35px;
    background: var(--status-bg);
    color: var(--white);
    font-size: 14px;
    display: flex;
    align-items: center;
    justify-content: space-between;
    padding: 0 10px;
  }
  .status-bar .signal { display: flex; align-items: center; gap: 6px; }
  .status-bar .battery { display: flex; align-items: center; gap: 5px; }

  .profile-header {
    height: 237px;
    background: var(--header-bg);
    position: relative;
  }
  .menu-toggle { position: absolute; left: 18px; top: 24px; }
  .profile-name {
    position: absolute; top: 42px; width: 100%;
    text-align: center; font-weight: 300; font-size: 24px;
    color: var(--text-dark);
  }
  .profile-avatar {
    position: absolute; left: 165px; top: 76px;
    width: 150px; height: 150px; border-radius: 50%;
    border: 6px solid var(--white);
    background: radial-gradient(circle at 50% 45%, var(--avatar-a), var(--avatar-b));
  }

  .create-game {
    height: 67px;
    background: var(--accent);
    color: var(--white);
    font-weight: 700; font-style: italic; font-size: 19px;
    display: flex; align-items: center; justify-content: center;
    letter-spacing: -0.2px;
  }

  .game-row {
    height: 162px;
    position: relative;
    border-bottom: 1px solid var(--divider);
  }
  .game-row:last-child { border-bottom: none; }
  .game-status {
    position: absolute; left: 22px; top: 18px;
    color: var(--accent); font-size: 19px; font-weight: 400;
    display: flex; align-items: center; gap: 6px;
  }
  .game-avatar {
    position: absolute; left: 22px; top: 48px;
    width: 90px; height: 90px; border-radius: 50%;
    background: radial-gradient(circle at 50% 45%, var(--avatar-a), var(--avatar-b));
  }
  .game-score {
    position: absolute; left: 128px; top: 64px;
    font-size: 40px; font-weight: 300; color: var(--text-dark);
    line-height: 1;
  }
  .game-opponent {
    position: absolute; left: 204px; top: 84px;
    font-size: 19px; font-style: italic; font-weight: 300; color: var(--text-dark);
  }
  .game-round {
    position: absolute; right: 22px; top: 88px;
    font-size: 15px; font-weight: 700; color: var(--text-muted);
  }

  .side-menu {
    position: absolute; left: 0; top: 35px; bottom: 0;
    width: 181px;
    background: var(--menu-bg);
    padding-top: 18px;
    list-style: none;
  }
  .side-menu li {
    height: 36px;
    padding-left: 22px;
    color: var(--white);
    font-size: 17px; font-weight: 700;
    display: flex; align-items: center;
    letter-spacing: -0.3px;
  }
  .side-menu li::before { content: ">"; font-size: 14px; margin-right: 7px; }
</style>
</head>
<body>

<!-- Home screen -->
<section class="screen screen--home">
  <div class="status-bar">
    <span class="signal">
      <svg width="52" height="10" viewBox="0 0 52 10"><g fill="#fff"><circle cx="5" cy="5" r="4"/><circle cx="15" cy="5" r="4"/><circle cx="25" cy="5" r="4"/><circle cx="35" cy="5" r="4"/></g><circle cx="45" cy="5" r="3.4" fill="none" stroke="#fff" stroke-width="1.2"/></svg>
      Carrier
    </span>
    <span class="time">5:30PM</span>
    <span class="battery">100%
      <svg width="30" height="14" viewBox="0 0 30 14"><rect x="0.5" y="0.5" width="26" height="13" rx="2" fill="none" stroke="#fff"/><rect x="2.5" y="2.5" width="22" height="9" fill="#fff"/><rect x="27.5" y="4.5" width="2" height="5" fill="#fff"/></svg>
    </span>
  </div>
  <header class="profile-header">
    <svg class="menu-toggle" width="28" height="18" viewBox="0 0 28 18"><g stroke="#333" stroke-width="1.6"><line x1="0" y1="1" x2="28" y2="1"/><line x1="0" y1="9" x2="28" y2="9"/><line x1="0" y1="17" x2="28" y2="17"/></g></svg>
    <h1 class="profile-name">Laura Brenner</h1>
    <div class="profile-avatar" role="img" aria-label="Profile photo of the player"></div>
  </header>
  <div class="create-game">&gt; CREATE NEW GAME</div>
  <div class="game-list">
    <article class="game-row">
      <div class="game-status"><svg width="8" height="12" viewBox="0 0 8 12"><path d="M0 0 L8 6 L0 12Z" fill="#a9cbd6"/></svg>My turn</div>
      <div class="game-avatar" role="img" aria-label="Opponent photo"></div>
      <div class="game-score">3 : 7</div>
      <div class="game-opponent">(Opponent)</div>
      <div class="game-round">ROUND 2</div>
    </article>
    <article class="game-row">
      <div class="game-status"><svg width="8" height="12" viewBox="0 0 8 12"><path d="M0 0 L8 6 L0 12Z" fill="#a9cbd6"/></svg>Wating for player</div>
      <div class="game-avatar" role="img" aria-label="Opponent photo"></div>
      <div class="game-score">3 : 7</div>
      <div class="game-opponent">(Opponent)</div>
      <div class="game-round">ROUND 2</div>
    </article>
    <article class="game-row">
      <div class="game-status"><svg width="8" height="12" viewBox="0 0 8 12"><path d="M0 0 L8 6 L0 12Z" fill="#a9cbd6"/></svg>Finished game</div>
      <div class="game-avatar" role="img" aria-label="Opponent photo"></div>
      <div class="game-score">3 : 7</div>
      <div class="game-opponent">(Opponent)</div>
      <div class="game-round">ROUND 2</div>
    </article>
  </div>
</section>

<!-- Home screen with side menu open -->
<section class="screen screen--menu">
  <div class="status-bar">
    <span class="signal">
      <svg width="52" height="10" viewBox="0 0 52 10"><g fill="#fff"><circle cx="5" cy="5" r="4"/><circle cx="15" cy="5" r="4"/><circle cx="25" cy="5" r="4"/><circle cx="35" cy="5" r="4"/></g><circle cx="45" cy="5" r="3.4" fill="none" stroke="#fff" stroke-width="1.2"/></svg>
      Carrier
    </span>
    <span class="time">5:30PM</span>
    <span class="battery">100%
      <svg width="30" height="14" viewBox="0 0 30 14"><rect x="0.5" y="0.5" width="26" height="13" rx="2" fill="none" stroke="#fff"/><rect x="2.5" y="2.5" width="22" height="9" fill="#fff"/><rect x="27.5" y="4.5" width="2" height="5" fill="#fff"/></svg>
    </span>
  </div>
  <header class="profile-header">
    <svg class="menu-toggle" width="28" height="18" viewBox="0 0 28 18"><g stroke="#333" stroke-width="1.6"><line x1="0" y1="1" x2="28" y2="1"/><line x1="0" y1="9" x2="28" y2="9"/><line x1="0" y1="17" x2="28" y2="17"/></g></svg>
    <h1 class="profile-name">Laura Brenner</h1>
    <div class="profile-avatar" role="img" aria-label="Profile photo of the player"></div>
  </header>
  <div class="create-game">&gt; CREATE NEW GAME</div>
  <div class="game-list">
    <article class="game-row">
      <div class="game-status"><svg width="8" height="12" viewBox="0 0 8 12"><path d="M0 0 L8 6 L0 12Z" fill="#a9cbd6"/></svg>My turn</div>
      <div class="game-avatar" role="img" aria-label="Opponent photo"></div>
      <div class="game-score">3 : 7</div>
      <div class="game-opponent">(Opponent)</div>
      <div class="game-round">ROUND 2</div>
    </article>
    <article class="game-row">
      <div class="game-status"><svg width="8" height="12" viewBox="0 0 8 12"><path d="M0 0 L8 6 L0 12Z" fill="#a9cbd6"/></svg>Wating for player</div>
      <div class="game-avatar" role="img" aria-label="Opponent photo"></div>
      <div class="game-score">3 : 7</div>
      <div class="game-opponent">(Opponent)</div>
      <div class="game-round">ROUND 2</div>
    </article>
    <article class="game-row">
      <div class="game-status"><svg width="8" height="12" viewBox="0 0 8 12"><path d="M0 0 L8 6 L0 12Z" fill="#a9cbd6"/></svg>Finished game</div>
      <div class="game-avatar" role="img" aria-label="Opponent photo"></div>
      <div class="game-score">3 : 7</div>
      <div class="game-opponent">(Opponent)</div>
      <div class="game-round">ROUND 2</div>
    </article>
  </div>
  <ul class="side-menu">
    <li>Overview</li>
    <li>My Groups</li>
    <li>Invite Friends</li>
    <li>Stats</li>
    <li>Help</li>
    <li>Imprint</li>
    <li>Signout</li>
  </ul>
</section>

</body>
</html>
```